Prairie Bend Comets

We are a travel softball organization based in Central IL. Girls are 8-14 yrs old. Looking for a modern website that is easily updated. Our current website is at www.prairiebendcomets-example.com. I want a tab for each team, 10U, 12U, 14U. I need a tab for pics. A tab for sponsors. A tap for files we have uploaded. And a about tab.

```html
<!DOCTYPE html>
<html lang="en">
<head>
<meta charset="utf-8">
<title>Prairie Bend Comets</title>
<link rel="stylesheet" href="https://fonts.googleapis.com/css2?family=Open+Sans:wght@300;400;700&display=swap">
<style>
  :root {
    --red: #ee3434;
    --caption-bg: #e1e2e4;
    --ink: #1a1a1a;
    --muted: #9a9a9c;
    --nav-bg: rgba(30, 30, 32, 0.72);
    --footer-bg: #3a3a3c;
    --white: #ffffff;
  }
  * { box-sizing: border-box; margin: 0; padding: 0; }
  html, body {
    width: 1155px; height: 1200px; overflow: hidden;
    background: var(--white);
    font-family: "Open Sans", Arial, sans-serif;
  }
  .page { position: relative; width: 1155px; height: 1200px; }

  .hero {
    position: absolute; left: 0; top: 0; width: 1155px; height: 490px;
    background:
      radial-gradient(ellipse 260px 300px at 720px 300px, rgba(40,140,70,0.85), transparent 70%),
      radial-gradient(ellipse 200px 220px at 90px 260px, rgba(170,60,40,0.7), transparent 70%),
      linear-gradient(180deg, #4c5250 0%, #2f3a36 45%, #23302c 100%);
  }
  .hero-shade { position: absolute; inset: 0; background: rgba(0,0,0,0.25); }

  .site-nav {
    position: absolute; left: 0; top: 0; width: 1155px; height: 96px;
    background: var(--nav-bg);
    display: flex; align-items: center;
  }
  .brand {
    position: absolute; left: 30px; top: 30px;
    display: flex; align-items: center; gap: 8px;
    color: var(--white); font-size: 24px; font-weight: 400; letter-spacing: 0.5px;
  }
  .brand-dot { width: 14px; height: 14px; border-radius: 50%; background: var(--red); }
  .nav-links {
    position: absolute; right: 40px; top: 38px;
    display: flex; gap: 24px; list-style: none;
    color: var(--white); font-size: 16px; font-weight: 400;
  }
  .nav-links .active { font-weight: 700; }

  .hero-statement {
    position: absolute; left: 357px; top: 162px; width: 440px;
    color: var(--white); text-align: center; text-transform: uppercase;
    font-size: 32px; line-height: 41px; font-weight: 400;
  }

  .section-title {
    position: absolute; left: 342px; top: 522px; width: 472px;
    display: flex; align-items: center; gap: 12px;
    font-size: 26px; font-weight: 700; color: var(--ink);
  }
  .section-title::before, .section-title::after {
    content: ""; flex: 1; height: 2px; background: var(--ink);
  }

  .team-card { position: absolute; top: 587px; width: 322px; }
  .team-photo {
    height: 321px; background: var(--red);
    display: flex; align-items: center; justify-content: center;
    color: var(--white); font-size: 34px; font-weight: 300;
  }
  .team-caption {
    height: 100px; background: var(--caption-bg); text-align: center;
    padding-top: 9px;
  }
  .team-name { font-size: 19px; font-weight: 700; color: #333; line-height: 22px; }
  .team-blurb { font-size: 18px; font-weight: 300; color: var(--muted); line-height: 17.5px; margin-top: 3px; }

  .back-to-top {
    position: absolute; left: 1036px; top: 1053px; width: 60px; height: 60px;
    background: #2d2d2f; display: flex; align-items: center; justify-content: center;
  }

  .site-footer {
    position: absolute; left: 0; top: 1135px; width: 1155px; height: 65px;
    background: var(--footer-bg);
  }
  .social { position: absolute; right: 28px; top: 20px; display: flex; gap: 20px; }
  .social span { width: 26px; height: 26px; border-radius: 50%; background: var(--white); display: block; }
</style>
</head>
<body>
<div class="page">
  <div class="hero" role="img" aria-label="Action photo of a softball batter running toward first base as teammates cheer from the dugout">
    <div class="hero-shade"></div>
  </div>

  <header class="site-nav">
    <div class="brand"><span class="brand-dot"></span>Comets</div>
    <ul class="nav-links">
      <li class="active">HOME</li>
      <li>CONTACT US</li>
      <li>SPONSORS</li>
      <li>ABOUT</li>
      <li>SCHEDULES &amp; RESULTS</li>
      <li>PICTURES/VIDEOS</li>
      <li>FILES</li>
    </ul>
  </header>

  <p class="hero-statement">Prairie Bend Comets is a girls travel softball organization based out of Prairie Bend, IL but with players from all over Central Illinois.</p>

  <h2 class="section-title">THE TEAMS</h2>

  <article class="team-card" style="left:79px">
    <div class="team-photo" role="img" aria-label="U10 team photo">PHOTO 1</div>
    <div class="team-caption">
      <h3 class="team-name">U10</h3>
      <p class="team-blurb">consectetur adipiscing elit,<br>sed do eiusmod tempor<br>incididunt ut labore...</p>
    </div>
  </article>
  <article class="team-card" style="left:418px">
    <div class="team-photo" role="img" aria-label="U12 team photo">PHOTO 2</div>
    <div class="team-caption">
      <h3 class="team-name">U12</h3>
      <p class="team-blurb">consectetur adipiscing elit,<br>sed do eiusmod tempor<br>incididunt ut labore...</p>
    </div>
  </article>
  <article class="team-card" style="left:757px">
    <div class="team-photo" role="img" aria-label="U14 team photo">PHOTO 3</div>
    <div class="team-caption">
      <h3 class="team-name">U14</h3>
      <p class="team-blurb">consectetur adipiscing elit,<br>sed do eiusmod tempor<br>incididunt ut labore...</p>
    </div>
  </article>

  <div class="back-to-top" aria-label="Back to top">
    <svg width="36" height="24" viewBox="0 0 36 24"><polyline points="3,21 18,6 33,21" fill="none" stroke="#fff" stroke-width="5"/></svg>
  </div>

  <footer class="site-footer">
    <div class="social" aria-label="Social links">
      <span></span><span></span><span></span>
    </div>
  </footer>
</div>
</body>
</html>
```